Re-design my 1-page website to be BETTER!

Hi Guys,
I recently created a 1-page website for market testing purposes for a company I am starting. Problem is, the feedback i've had on the page is its a bit corporate and boring.
I would love you to design something that is fresher, more modern and will generate leads (via the sign up CTA's).
Here is the website as it is now: www.guidelinkhub.com.au.
If you need any info or have questions, just reach out.
Thanks,
Oliver

Target Market(s)

Entrepreneurs

Number of Pages Required

1 page

Font styles to use
Sans Serif

Colors
abd036
34a6d7
ffffff

Requirements
Must have
• Fresh, Modern, high-converting
• I expect 70% of traffic to be mobile so must be mobile optimised first.
Nice to have
• I've highlighted colours i like below, however, I am open to suggestions. I like colours that are gender neutral and show energy and vibrancy.
• I have used Proxima Nova for the fonts, as I find it easy to read however, I am open to suggestions. My main preference is that it displays well and is easily read

```html
<!DOCTYPE html>
<html lang="en">
<head>
<meta charset="utf-8">
<title>Guidelink Hub</title>
<link rel="stylesheet" href="https://fonts.googleapis.com/css2?family=Mulish:wght@300;400;600;700&family=Roboto:wght@300;400;700&display=swap">
<style>
:root{
  --green:#abd036;
  --blue:#34a6d7;
  --white:#ffffff;
  --light:#f2f2f2;
  --ink:#333333;
  --body:#555555;
  --faq-body:#8fd8f7;
  --hero-dark:#2a221c;
}
*{box-sizing:border-box;margin:0;padding:0}
html,body{width:1200px;height:2877px;overflow:hidden}
body{position:relative;font-family:"Mulish",sans-serif;color:var(--ink);background:var(--white)}
.abs{position:absolute}

.brand{font-weight:400;color:var(--white);font-size:38px;line-height:46px;display:flex;align-items:center;gap:14px}
.brand-mark{width:22px;height:22px;background:var(--white)}

/* hero */
.hero-photo{left:0;top:0;width:1200px;height:437px;background:linear-gradient(135deg,#2a221c 0%,#4a3a2e 45%,#1f1a17 100%)}
.signup{left:875px;top:39px;width:99px;height:28px;background:var(--blue);color:var(--white);font-size:12px;font-weight:600;display:flex;align-items:center;justify-content:center}
.hero-title{left:560px;width:415px;top:189px;text-align:right;color:var(--white);font-family:"Roboto",sans-serif;font-size:21px;line-height:26px}
.quote{left:560px;top:229px;width:415px;height:120px;border:3px solid var(--white);color:var(--white);font-family:"Roboto",sans-serif;font-weight:300;font-size:15px;line-height:20px;text-align:center;padding:13px 22px 0}
.quote cite{display:block;text-align:right;font-style:normal;font-weight:700;font-size:12px;margin-top:9px}

/* intro */
.intro{left:0;top:437px;width:1200px;height:363px;background:var(--light)}
.section-title{left:0;width:1200px;text-align:center;font-weight:400;font-size:26px;line-height:32px;color:#444}
.lead-form{left:225px;top:562px;width:265px;height:188px;background:var(--green);border:1px solid #9bbf2c;padding:32px 13px 0}
.field{height:28px;background:var(--white);border-radius:3px;font-size:10px;color:#999;padding:7px 12px;margin-bottom:13px}
.submit{position:absolute;right:13px;top:123px;width:113px;height:34px;border:2px solid var(--white);border-radius:3px;color:var(--white);font-size:18px;display:flex;align-items:center;justify-content:center}
.intro-copy{left:508px;top:562px;width:466px;font-family:"Roboto",sans-serif;font-weight:300;font-size:12px;line-height:19px;text-align:center;color:var(--body)}
.intro-copy p{padding:0 4px}
.highlight{background:var(--blue);color:var(--white);font-weight:400;padding:6px 8px !important;margin:10px 0 12px}

/* invest */
.invest-photo{left:0;top:800px;width:1200px;height:373px;background:linear-gradient(100deg,#2b2a24 0%,#3c3a31 50%,#23221d 100%)}
.invest-title{left:225px;top:877px;color:var(--white);font-weight:400;font-size:34px;line-height:42px}
.invest-copy{left:225px;width:440px;color:var(--white);font-size:12.5px;line-height:18px}
.register{left:225px;top:1056px;width:185px;height:41px;background:var(--blue);color:var(--white);font-size:16px;display:flex;align-items:center;justify-content:center}

/* steps */
.subtitle{left:0;width:1200px;top:1279px;text-align:center;font-size:12.5px;line-height:16px}
.step{width:220px;text-align:center}
.step-icon{height:46px;margin:0 auto 22px}
.step h3{font-weight:400;font-size:13px;line-height:16px}
.step hr{width:50px;border:0;border-top:3px solid #c9c9c9;margin:12px auto 14px}
.step p{font-family:"Roboto",sans-serif;font-weight:300;font-size:11.5px;line-height:14.5px;color:var(--body)}

/* benefits */
.benefits{left:0;top:1647px;width:1200px;height:512px;background:var(--green)}
.person-photo{left:45px;top:1584px;width:324px;height:575px;background:linear-gradient(180deg,#4b5566 0%,#2a3852 100%)}
.card{width:365px;height:137px;text-align:center;padding:0 16px;display:flex;flex-direction:column;justify-content:center}
.card-white{background:rgba(255,255,255,.88)}
.card-tint{background:rgba(255,255,255,.7)}
.card h3{font-weight:400;font-size:14px;line-height:18px;margin-bottom:11px}
.card p{font-family:"Roboto",sans-serif;font-weight:300;font-size:11px;line-height:14.5px;color:var(--body)}

/* faq */
.faq-item{height:40px;background:var(--blue);color:var(--white);font-size:13.5px;padding:0 14px;display:flex;align-items:center;justify-content:space-between}
.faq-body{height:187px;background:var(--faq-body);font-family:"Roboto",sans-serif;font-weight:300;font-size:11px;line-height:17.5px;color:var(--ink);padding:9px 14px}

/* footer */
.footer{left:0;top:2676px;width:1200px;height:201px;background:var(--green)}
.footer-brand{left:0;width:1200px;top:2713px;justify-content:center;font-size:40px}
.tagline{left:0;width:1200px;top:2786px;text-align:center;color:var(--white);font-size:15.5px;font-weight:600}
.rule{left:0;top:2846px;width:1200px;height:1px;background:rgba(255,255,255,.6)}
.copyright{left:0;width:1200px;top:2857px;text-align:center;color:var(--white);font-size:9px}
</style>
</head>
<body>

<!-- hero -->
<div class="abs hero-photo" role="img" aria-label="Photo of a desk with notebooks, glasses, a drink and a laptop"></div>
<div class="abs brand" style="left:226px;top:30px"><span class="brand-mark"></span>Guidelink Hub</div>
<div class="abs signup">Sign Up</div>
<div class="abs hero-title">A Mentor For Everyone</div>
<div class="abs quote">"We've flipped the model on its head - so now you choose your Mentor. It's never been this easy to get the advice and guidance you need to thrive"<cite>- Oliver, Founder - Guidelink Hub</cite></div>
<svg class="abs" style="left:860px;top:346px" width="40" height="32" viewBox="0 0 40 32"><polygon points="2,1 36,1 36,30" fill="#2a221c"/><polyline points="2,2 36,29 36,2" fill="none" stroke="#fff" stroke-width="3"/></svg>

<!-- intro -->
<section class="abs intro"></section>
<h2 class="abs section-title" style="top:487px">Finding a Mentor Has Never Been Easier</h2>
<form class="abs lead-form">
  <div class="field">Enter your name</div>
  <div class="field">Enter your Email-ID</div>
  <div class="submit">Submit</div>
</form>
<div class="abs intro-copy">
  <p>Having a great Mentor will turbo-charge your personal, professional or business growth. But unless you have an incredible network, finding great Mentors has always been a challenge.</p>
  <p class="highlight">Guidelink Hub changes all that, levelling the playing field and making it easy for entrepreneurs and professionals to find the advice and guidance they deserve.</p>
  <p>No longer will you have to go searching for your perfect Mentor. We bring the perfect Mentor to you, selected from a global pool of experts, putting the power back in your hands and letting you get on with your growth.</p>
</div>

<!-- invest -->
<div class="abs invest-photo" role="img" aria-label="Photo of a mentor talking with a client in a café"></div>
<h2 class="abs invest-title">It's Time to Invest in You</h2>
<p class="abs invest-copy" style="top:936px">If you've come this far you've already taken the most important step: recognising how mentorship can help you; and taking action to find it. And now your here, the rest is easy.</p>
<p class="abs invest-copy" style="top:1007px"><strong>Get started now</strong> and let Guidelink Hub do the rest...</p>
<div class="abs register">Register Now</div>

<!-- steps -->
<h2 class="abs section-title" style="top:1224px">Mentorship: But Different</h2>
<p class="abs subtitle">Finding a Mentor used to be hard; but not any more.<br>We've turned the traditional model on its head, so now Mentors seek you.</p>
<div class="abs step" style="left:233px;top:1350px">
  <div class="step-icon" role="img" aria-label="Icon of a person writing a list" style="width:44px;background:#3a7bd5"></div>
  <h3>Tell Us What You Need</h3><hr>
  <p>There is no one size fits all approach to Mentorship. So tell us the challenges you are facing and the skill-set your Mentor must have.</p>
</div>
<div class="abs step" style="left:490px;top:1350px">
  <div class="step-icon" role="img" aria-label="Icon of a mentor on a screen" style="width:60px;background:#2ec4d8"></div>
  <h3>Choose Your Mentor</h3><hr>
  <p>Mentors are invited to Mentor you. We select 3 top picks that align with your criteria. It's then up to you whether you choose a Mentor, interview 1 or more or refine your criteria and start again.</p>
</div>
<div class="abs step" style="left:746px;top:1350px">
  <div class="step-icon" role="img" aria-label="Icon of a monitor with tools" style="width:50px;background:#2e6ab8"></div>
  <h3>Ongoing Support</h3><hr>
  <p>We don't stop once you have your perfect Mentor. We're on hand to make life easy for you, keep your sessions on track and provide ongoing support.</p>
</div>

<!-- benefits -->
<section class="abs benefits"></section>
<svg class="abs" style="left:0;top:1647px" width="1200" height="512"><polygon points="0,0 22,0 916,512 0,512" fill="#34a6d7"/></svg>
<div class="abs person-photo" role="img" aria-label="Photo of a smiling bearded man in a blazer presenting with an open hand"></div>
<div class="abs card card-white" style="left:397px;top:1679px"><h3>Impartial Advice</h3><p>Imagine being able to speak to someone who has been through the challenges you are currently facing? Who has "been there seen that" and can help you navigate the ups and downs of your career or business?</p></div>
<div class="abs card card-tint" style="left:780px;top:1679px"><h3>Avoid the Pitfalls</h3><p>Running a business and the challenges of corporate life can be extremely stressful. And often, our friends and family just don't get it. So imagine having someone independent who can understand where your coming from and, help you see things objectively.</p></div>
<div class="abs card card-tint" style="left:397px;top:1834px"><h3>A Supportive Ear</h3><p>Running a business and the challenges of corporate life can be extremely stressful. And often, our friends and family just don't get it. So imagine having someone independent who can understand where your coming from and, help you see things objectively.</p></div>
<div class="abs card card-tint" style="left:780px;top:1834px"><h3>Clarity</h3><p>Sometimes we are so caught up in our own world we struggle to see the big picture. You Mentor will provide an objective, outsider view. Helping you to cut though the noise and focus on what's really important.</p></div>
<div class="abs card card-white" style="left:397px;top:1990px"><h3>Motivation</h3><p>Your Mentor has seen this before and been in your shoes. They understand what your going through and will help you to re-focus and re-energise.</p></div>
<div class="abs card card-tint" style="left:780px;top:1990px"><h3>Make you Accountable</h3><p>A Mentor is not just there to pick you up - they are to give honest appraisal and tell you when your falling short. Ultimately, only you can control your success and you Mentor will hold you accountable to make sure you are.</p></div>

<!-- faq -->
<h2 class="abs section-title" style="top:2209px">FAQ</h2>
<div class="abs" style="left:225px;top:2281px;width:365px">
  <div class="faq-item">What is a Mentor?<svg width="12" height="8"><polyline points="1,1 6,6 11,1" fill="none" stroke="#fff" stroke-width="1.6"/></svg></div>
  <div class="faq-body">Experienced and Trusted Advisor. Guru. Confidente. Friend.<br>In essence a Mentor is someone who can turn to for guidance and advice.Someone who is more experienced than you and, has navigated similar challenges to you and can foresee the pitfalls and hurdles you face.A great Mentor is also a motivator, connector and guide. Will help you focus on what's really important and see the bigger picture.Importantly, a great Mentor should be outside your immediate network of friends and relatives. And, be able to offer unbiased, honest and objective advice, that you can action.</div>
</div>
<div class="abs faq-item" style="left:225px;top:2527px;width:365px">What if it doesn't work out?<svg width="8" height="12"><polyline points="1,1 6,6 1,11" fill="none" stroke="#fff" stroke-width="1.6"/></svg></div>
<div class="abs faq-item" style="left:225px;top:2587px;width:365px">How do we meet?<svg width="8" height="12"><polyline points="1,1 6,6 1,11" fill="none" stroke="#fff" stroke-width="1.6"/></svg></div>
<div class="abs faq-item" style="left:609px;top:2281px;width:365px">Is a Mentor right for me?<svg width="8" height="12"><polyline points="1,1 6,6 1,11" fill="none" stroke="#fff" stroke-width="1.6"/></svg></div>
<div class="abs faq-item" style="left:609px;top:2340px;width:365px">How often do we meet?<svg width="8" height="12"><polyline points="1,1 6,6 1,11" fill="none" stroke="#fff" stroke-width="1.6"/></svg></div>
<div class="abs faq-item" style="left:609px;top:2400px;width:365px">Can I have more than one Mentor?<svg width="8" height="12"><polyline points="1,1 6,6 1,11" fill="none" stroke="#fff" stroke-width="1.6"/></svg></div>
<div class="abs faq-item" style="left:609px;top:2459px;width:365px">What are the costs?<svg width="8" height="12"><polyline points="1,1 6,6 1,11" fill="none" stroke="#fff" stroke-width="1.6"/></svg></div>

<!-- footer -->
<footer class="abs footer"></footer>
<div class="abs brand footer-brand"><span class="brand-mark"></span>Guidelink Hub</div>
<p class="abs tagline">Sign up is free, obligation free and 100% confidential</p>
<div class="abs rule"></div>
<p class="abs copyright">Copyright© All rights reserved</p>

</body>
</html>
```